Want to fly? Flight school needs a roll up

Hello designers

We are a small aviation club with around 100 members. We love flying and therefore offer free flight lessons for young people at our glider flight school.
The young people only have to pay a flat rate of €300 for the aircraft until their first solo flight.
To advertise the flight school we now need a roll up banner measuring 85cm x 200cm. You can find the data sheet for the banner in the appendix.
Content of the roll up banner:
Advertising for our flight school so that we can attract new members
The banner should be designed in our club colors blue/white
The banner is aimed at all people who want to get a glider license
A great offer for young people up to the age of 25 should be placed on the banner with a reference to the text “Offer only applies to people up to the age of 25. Included in the flat rate of €300 is training on the glider up to the first "solo flight"
The banner is intended to advertise training with a glider. Therefore the wish would be for a glider to be depicted

Here is a link to our current homepage

https://www.lsg-tarnhofen.de/

https://www.vidoplex.example/watch?v=K8p2Qz4LmXc

Target Market(s)

Young people from 14 years to 30 years

Colors
0054AA
0677BA
7BADD7
CADEEF
E8F1F8

Requirements
Nice to have
• Glider / club logo
Should not have
• Too much text

```html
<!DOCTYPE html>
<html lang="en">
<head>
<meta charset="utf-8">
<title>Free Flight Lessons – Roll Up</title>
<link rel="stylesheet" href="https://fonts.googleapis.com/css2?family=Oswald:wght@400;500;700&family=Roboto+Condensed:wght@400;700&display=swap">
<style>
  :root{
    --blue-deep:#0a2a8a;
    --blue:#0054AA;
    --blue-mid:#0677BA;
    --blue-light:#7BADD7;
    --blue-pale:#CADEEF;
    --blue-mist:#E8F1F8;
    --red:#c8102e;
    --red-dark:#8f0a1f;
    --gold:#f5b800;
    --white:#ffffff;
    --ink:#1b2340;
  }
  *{margin:0;padding:0;box-sizing:border-box}
  html,body{width:686px;height:1200px;overflow:hidden;background:var(--white)}
  .banner{position:relative;width:686px;height:1200px;overflow:hidden;background:var(--white);font-family:"Oswald",sans-serif;color:var(--ink)}
  .header-swoosh{position:absolute;left:0;top:0;width:686px;height:230px}
  .club-mark{position:absolute;left:273px;top:28px;width:140px;height:140px;border-radius:50%;background:var(--white);border:4px solid var(--blue);display:flex;align-items:center;justify-content:center;text-align:center;z-index:3}
  .club-mark span{font-family:"Oswald",sans-serif;font-weight:700;font-size:20px;line-height:1.1;color:var(--blue)}
  .photo-crowd{position:absolute;left:0;top:190px;width:686px;height:250px;background:linear-gradient(180deg,#5d9ad8 0%,#a9cdef 45%,#7fa05a 62%,#4f7a33 100%);z-index:1}
  .pilot-badge{position:absolute;left:263px;top:355px;width:160px;height:160px;border-radius:50%;background:var(--red);border:6px solid var(--white);box-shadow:0 4px 10px rgba(0,0,0,.25);display:flex;flex-direction:column;align-items:center;justify-content:center;color:var(--white);text-transform:uppercase;text-align:center;z-index:4}
  .pilot-badge .small{font-size:22px;font-weight:500;line-height:1.05}
  .pilot-badge .big{font-size:34px;font-weight:700;line-height:1.05}
  .headline{position:absolute;left:0;top:528px;width:686px;display:flex;justify-content:center;align-items:center;gap:14px;color:var(--blue-deep);text-transform:uppercase}
  .headline .free{font-size:104px;font-weight:700;line-height:.9}
  .headline .stack{display:flex;flex-direction:column;line-height:.92}
  .headline .flight{font-size:60px;font-weight:700}
  .headline .lessons{font-size:42px;font-weight:400;letter-spacing:2px}
  .headline-rule{position:absolute;left:277px;top:636px;width:132px;height:8px;background:var(--red)}
  .subline{position:absolute;left:0;top:656px;width:686px;text-align:center;font-family:"Roboto Condensed",sans-serif;font-weight:700;font-size:27px;line-height:1.2;color:var(--ink);text-transform:uppercase}
  .photo-glider{position:absolute;left:330px;top:730px;width:356px;height:110px;background:linear-gradient(180deg,#dfe9f3 0%,#c5d3de 55%,#8ea06c 100%);z-index:2}
  .offer-panel{position:absolute;left:0;top:760px;width:686px;height:440px}
  .price{position:absolute;left:46px;top:842px;font-size:104px;font-weight:700;color:var(--white);line-height:1;z-index:3}
  .price-note{position:absolute;left:268px;top:862px;color:var(--white);text-transform:uppercase;z-index:3}
  .price-note .lead{font-family:"Roboto Condensed",sans-serif;font-size:22px;line-height:1.15}
  .price-note .solo{font-size:48px;font-weight:700;color:var(--gold);line-height:1.05}
  .age-ribbon{position:absolute;left:60px;top:972px;width:566px;height:78px;background:var(--red);color:var(--white);display:flex;align-items:center;justify-content:center;text-align:center;font-family:"Roboto Condensed",sans-serif;font-weight:700;font-size:27px;line-height:1.15;text-transform:uppercase;z-index:3}
  .train{position:absolute;left:250px;top:1068px;width:436px;text-align:center;color:var(--white);font-size:36px;font-weight:500;letter-spacing:1px;text-transform:uppercase;z-index:3}
  .photo-instructor{position:absolute;left:0;top:1060px;width:230px;height:140px;background:linear-gradient(180deg,#c9d6e2 0%,#9fb2c4 60%,#5a6c80 100%);z-index:2}
  .booking{position:absolute;right:40px;top:1122px;text-align:right;text-transform:uppercase;z-index:3}
  .booking .label{font-size:30px;font-weight:500;color:var(--gold);letter-spacing:2px;line-height:1.1}
  .booking .url{font-family:"Roboto Condensed",sans-serif;font-size:26px;font-weight:700;color:var(--white);text-transform:none;line-height:1.2}
</style>
</head>
<body>
<div class="banner">
  <svg class="header-swoosh" viewBox="0 0 686 230" aria-hidden="true">
    <path d="M0 120 Q343 250 686 120 L686 210 L0 210 Z" fill="var(--blue-deep)"/>
    <path d="M0 145 Q343 260 686 145 L686 210 L0 210 Z" fill="var(--blue-mid)"/>
    <path d="M0 165 Q343 270 686 165 L686 210 L0 210 Z" fill="var(--white)"/>
  </svg>

  <div class="club-mark"><span>LSG<br>Tarnhofen</span></div>

  <div class="photo-crowd" role="img" aria-label="Photo of visitors gathered on a grass airfield under a blue sky"></div>

  <div class="pilot-badge">
    <span class="small">Become</span>
    <span class="big">A Pilot</span>
    <span class="small">Now!</span>
  </div>

  <div class="headline">
    <span class="free">Free</span>
    <span class="stack"><span class="flight">Flight</span><span class="lessons">Lessons</span></span>
  </div>
  <div class="headline-rule"></div>

  <p class="subline">For young people at our glider<br>flight school</p>

  <svg class="offer-panel" viewBox="0 0 686 440" aria-hidden="true">
    <defs>
      <linearGradient id="offerFill" x1="0" y1="0" x2="0" y2="1">
        <stop offset="0" stop-color="var(--blue)"/>
        <stop offset="1" stop-color="var(--blue-deep)"/>
      </linearGradient>
    </defs>
    <path d="M0 30 Q343 -10 686 40 L686 440 L0 440 Z" fill="var(--blue-light)"/>
    <path d="M0 50 Q343 10 686 60 L686 440 L0 440 Z" fill="url(#offerFill)"/>
  </svg>

  <div class="photo-glider" role="img" aria-label="Photo of a white and red aircraft parked on an airfield"></div>

  <div class="price">€300</div>
  <div class="price-note">
    <div class="lead">For the aircraft until<br>their first</div>
    <div class="solo">Solo Flight</div>
  </div>

  <div class="age-ribbon">Offer only applies to people<br>up to the age of 25</div>

  <div class="train">Train with a glider</div>

  <div class="photo-instructor" role="img" aria-label="Photo of a club flight instructor"></div>

  <div class="booking">
    <div class="label">Book Online</div>
    <div class="url">www.lsg-tarnhofen.de</div>
  </div>
</div>
</body>
</html>
```